direct mail piece for 2 automotive direct mailer 8.5 x 11 tri fold that fit in a envelope with a st

i need a mailer done for an automotive mailer i have the copy of an older version that i need updated and done quickly.

i think its a very simple task

i also have a log in for the ad planer for pictures and such
Updates

i have all the logos needed and ad planners for both projects . one project is for a Tarvel Brennick store- the other is For a Dravonette storeĀ 

Target Market(s)

mailing to a house list or people that have already bought a car or had service work who want to trade in there current vehicle

Industry/Entity Type

Automotive

Colors
3277b5

Requirements
Must have
• creative mind

inclosed is the copy and there is a Dennis P Orwell tarvel Brennick logo that needs to be added

oem logos
Nice to have
• follow thru person , understand how to get a prospect into a buyer
Should not have
• lazyness

```html
<!DOCTYPE html>
<html lang="en">
<head>
<meta charset="utf-8">
<title>Vehicle Termination Option – Event Mailer</title>
<link rel="stylesheet" href="https://fonts.googleapis.com/css2?family=Source+Sans+3:wght@300;400;600;700&family=Crimson+Text:ital,wght@0,400;0,700;1,400;1,700&family=Mrs+Saint+Delafield&display=swap">
<style>
  :root {
    --red: #d11f3a;
    --red-dark: #a3122a;
    --red-deep: #8c0f22;
    --blue: #2f4f9e;
    --ink: #1e1e1e;
    --grey: #555555;
    --paper: #ffffff;
    --paper-shade: #ebebeb;
    --photo-dark: #1a1613;
    --photo-mid: #5a4a3c;
    --photo-light: #b49a7e;
  }
  * { margin: 0; padding: 0; box-sizing: border-box; }
  html, body { width: 900px; height: 1200px; overflow: hidden; background: var(--paper); }
  .mailer {
    position: relative;
    width: 900px;
    height: 1200px;
    overflow: hidden;
    background: linear-gradient(180deg, var(--paper-shade) 0%, var(--paper) 18%, var(--paper) 80%, var(--paper-shade) 100%);
    font-family: "Crimson Text", Georgia, serif;
    color: var(--ink);
  }
  .hero-photo {
    position: absolute;
    left: 0; top: 0;
    width: 900px; height: 300px;
    background:
      radial-gradient(ellipse 260px 150px at 600px 130px, #2a2a2e 0%, #151518 60%, transparent 100%),
      linear-gradient(100deg, var(--photo-light) 0%, var(--photo-mid) 25%, var(--photo-dark) 50%, var(--photo-mid) 80%, var(--photo-light) 100%);
  }
  .banner { position: absolute; left: 0; top: 180px; }
  .headline {
    position: absolute;
    left: 52px; top: 208px;
    font-family: "Source Sans 3", Arial, sans-serif;
    font-weight: 700;
    line-height: 1;
  }
  .headline .word-white { display: block; color: var(--paper); font-size: 66px; letter-spacing: -0.5px; }
  .headline .word-blue {
    display: block;
    color: var(--blue);
    font-size: 70px;
    font-weight: 600;
    letter-spacing: -1.5px;
    transform: scaleX(0.98);
    transform-origin: left;
    margin: -4px 0 -6px;
  }
  .headline .option-line { display: flex; align-items: center; gap: 6px; }
  .offer {
    position: absolute;
    left: 560px; top: 244px;
    width: 335px;
    color: var(--paper);
    font-family: "Source Sans 3", Arial, sans-serif;
  }
  .offer .lead { font-size: 17px; line-height: 25px; }
  .offer .prize {
    margin-top: 10px;
    margin-left: -12px;
    width: 340px;
    text-align: center;
    font-weight: 400;
    font-size: 41px;
    line-height: 35px;
  }
  .offer .prize sup { font-size: 13px; vertical-align: super; line-height: 0; }
  .letter {
    position: absolute;
    left: 53px; top: 478px;
    width: 830px;
    font-size: 17px;
    letter-spacing: 0.2px;
    line-height: 22.5px;
    white-space: nowrap;
  }
  .letter .greeting { margin-bottom: 21px; }
  .letter .para-1 { margin-bottom: 23px; }
  .letter .para-2 { margin-bottom: 16px; }
  .letter .para-3 { margin-bottom: 20px; }
  .letter .para-4 { margin-bottom: 15px; }
  .footer-swoosh { position: absolute; left: 0; top: 1100px; }
  .sign-off { position: absolute; left: 53px; top: 974px; font-size: 17px; }
  .signature {
    position: absolute;
    left: 53px; top: 1008px;
    font-family: "Mrs Saint Delafield", cursive;
    font-size: 40px;
    line-height: 1;
  }
  .signer { position: absolute; left: 53px; top: 1045px; font-style: italic; font-size: 17px; }
  .fine-print {
    position: absolute;
    left: 53px; top: 1082px;
    width: 468px;
    font-size: 9.6px;
    line-height: 12.5px;
    font-style: italic;
    font-weight: 700;
    text-align: justify;
  }
  .event-dates {
    position: absolute;
    left: 505px; top: 974px;
    width: 360px;
    text-align: center;
    font-weight: 700;
  }
  .event-dates .days { font-size: 32px; line-height: 38px; }
  .event-dates .hours { font-size: 29px; line-height: 34px; }
  .event-dates .note { font-size: 8.5px; font-style: italic; font-weight: 400; line-height: 10px; }
  .contact {
    position: absolute;
    left: 553px; top: 1094px;
    font-family: "Source Sans 3", Arial, sans-serif;
    color: var(--ink);
  }
  .contact .cta { font-size: 18px; letter-spacing: 0.5px; line-height: 22px; }
  .contact .phone { font-size: 33px; font-weight: 400; line-height: 38px; }
  .dealer-name {
    position: absolute;
    left: 780px; top: 1108px;
    width: 100px;
    text-align: center;
    font-family: "Source Sans 3", Arial, sans-serif;
    font-weight: 600;
    font-size: 24px;
    color: var(--ink);
  }
  .dealer-line {
    position: absolute;
    left: 536px; top: 1158px;
    font-family: "Source Sans 3", Arial, sans-serif;
    font-size: 12.5px;
    color: var(--grey);
    display: flex; align-items: center; gap: 12px;
  }
  .dealer-line .divider { width: 2px; height: 15px; background: var(--red); }
</style>
</head>
<body>
<main class="mailer">
  <div class="hero-photo" role="img" aria-label="Dark Tarvel sedan driving at night with blurred city lights behind it"></div>

  <svg class="banner" width="900" height="270" viewBox="0 0 900 270" aria-hidden="true">
    <polygon points="0,40 900,25 900,235 0,262" fill="var(--red-deep)"/>
    <polygon points="0,8 495,22 528,218 0,262" fill="var(--red)"/>
    <polygon points="492,52 900,36 900,232 548,248" fill="var(--red)"/>
    <polygon points="495,22 528,218 548,248 492,52" fill="var(--red-dark)"/>
  </svg>

  <h1 class="headline">
    <span class="word-white">Vehicle</span>
    <span class="word-blue">TERMINATION</span>
    <span class="option-line">
      <span class="word-white">Option</span>
      <svg width="74" height="68" viewBox="0 0 74 68" aria-hidden="true">
        <circle cx="34" cy="37" r="28" fill="none" stroke="var(--blue)" stroke-width="3.5"/>
        <path d="M18 37 L31 51 L68 6" fill="none" stroke="var(--blue)" stroke-width="5" stroke-linecap="round" stroke-linejoin="round"/>
      </svg>
    </span>
  </h1>

  <section class="offer">
    <p class="lead">As a preferred customer, just for coming in during this event, you will receive a</p>
    <p class="prize">3 DAY/ 2 NIGHT<br>VACTION<br>FOR TWO<sup>(3)</sup></p>
  </section>

  <article class="letter">
    <p class="greeting">Harcia pro dolorias ant.</p>
    <p class="para-1">Sed quodigent peliquam et que as pres vollaci con eum evendit a atus etus, nate volores tibusame susdae volore,<br>sequia dentio. Et lant harios eati unt re illis nis voluptatur? Bo. Onserun ducient pratiatis dendit rat omnihitaspe</p>
    <p class="para-2">moluptatis etur architа que nus, vendes untiisciis et laborroviti omnimag nisqui ut eossi nos sapid minveles dolla<br>quo quos ulpa dolecabor aut qui autem consequiam entemqui dolupta si anto dit hition pedit explici aspidip sun-<br>dae dit optat evelecab isqui ommodigendem de dolo ma des nonet ad minctorro velis unt, cuptatur aut aut acep-<br>ero viducitatur millab inci sitionsequam sus et aut ende repero est, ad ute con corepel loreriam elit, cuptatem et</p>
    <p class="para-3">am libus minci sit, sum ium dellit pelit magnis soloreius evelendem aturiatis rescienis am, tem harum, comnime<br>perita eatium site nietum que veliquam nus ut lacienis intio commodit unt dolorem quibusae re vit ulpario. Os<br>maiore, quidem idunt.Rovitas sitium re nonem eum, ipsa con earunda non et accaerrorrum atusci dit et moditae<br>delibus, od mo es eosapid magnataspit ommodis eratquas ent labo. Itatur, a pe nemodi acid maxime non.</p>
    <p class="para-4">blaborerum fuga. Et aut aceped ullabor ibusdam voluptae exceperatur alignatumqui dolum, volor audam esequas<br>inciatur aperumq uaeceaqui dolorporem liquibus sunt quibusdae. Genis accusda ea natem fuga. Dunt.<br>Gendam quam fuga. Et fugiam hitatia eliquid militis et et, sumquas venist, qui doluptaspe doluptat.</p>
    <p>Necae commolu ptatur aut fuga. Possinv enimustrum exero is cores alit occaborum ut audicate doluptatque re-<br>pudipsant essit, volo quo que lautemped et volupta simendenia que cumqui doluptaturis dolumqu aectam elique<br>nihilit voluptatum faces essusamet, quodis sandebist, culloreicia cum nim vercilla sunte expliqui a berferum.</p>
  </article>

  <svg class="footer-swoosh" width="525" height="100" viewBox="0 0 525 100" aria-hidden="true">
    <path d="M0 20 C150 55 320 70 525 76 L525 100 L0 100 Z" fill="var(--red)"/>
    <path d="M0 12 C150 48 320 64 525 70" fill="none" stroke="var(--red-dark)" stroke-width="1.5"/>
  </svg>

  <p class="sign-off">Sincerly,</p>
  <p class="signature">Theo Marlow</p>
  <p class="signer">Theo Marlow - Business Development Manager</p>
  <p class="fine-print">Offer valid for current owners only with approved credit. Vacation certificate is limited to one per household and requires attendance during the event dates. Travel restrictions apply and blackout dates may change without notice. Trade values depend on vehicle condition, mileage and market demand. Prior sales are excluded from this program. See dealer for full details on terms, eligibility and program rules. Tax, title, license and dealer fees are extra. Photos are for illustration only. Not all buyers will qualify for every offer. Offer ends on the final event date and cannot be combined with others.</p>

  <section class="event-dates">
    <p class="days">July 12, 13, and 14, 2014</p>
    <p class="hours">9:00 a.m. to 10:00 p.m.</p>
    <p class="note">After these dates, normal pricing resumes.</p>
  </section>

  <section class="contact">
    <p class="cta">CALL US NOW</p>
    <p class="phone">(208) 555-0143</p>
  </section>

  <p class="dealer-name">Merrin</p>

  <p class="dealer-line">
    <span>Dennis Orwell Merrin</span>
    <span class="divider"></span>
    <span>4120 Calder Lane, Meridale, ID 83700</span>
  </p>
</main>
</body>
</html>
```